Business Card Design Project

Hi I am after a business card double sided 1 side to have the attached PDF on front on the back:

Dace Marlowby - Managing Director
Mobile: 0413 286 451
email: dace@vrum.com.au
web: www.vrum.com.au

Industry/Entity Type

Business

Font styles to use
Sans Serif

Requirements
Must have
• I want a classy looking card
Nice to have
• I like lime green and black and white

```html
<!DOCTYPE html>
<html lang="en">
<head>
<meta charset="utf-8">
<title>Verum Lawns and Grounds – Business Card</title>
<link rel="stylesheet" href="https://fonts.googleapis.com/css2?family=Questrial&family=Urbanist:wght@700&display=swap">
<style>
  :root {
    --stage: #d1d2d4;
    --card: #ffffff;
    --green: #2bb34c;
    --ink: #000000;
    --paper: #ffffff;
  }
  * { margin: 0; padding: 0; box-sizing: border-box; }
  html, body {
    width: 1200px;
    height: 986px;
    overflow: hidden;
    background: var(--stage);
  }
  .card {
    position: absolute;
    left: 88px;
    top: 220px;
    width: 1049px;
    height: 601px;
    background: var(--card);
    font-family: "Questrial", "Century Gothic", sans-serif;
    color: var(--ink);
  }
  .brand {
    position: absolute;
    left: 0;
    right: 0;
    top: 88px;
    display: flex;
    align-items: center;
    justify-content: center;
    gap: 22px;
  }
  .brand-square {
    width: 78px;
    height: 78px;
    background: var(--green);
    border-radius: 10px;
  }
  .brand-name {
    font-size: 42px;
    color: var(--ink);
    letter-spacing: 0.2px;
  }
  .name-band {
    position: absolute;
    left: 0;
    top: 293px;
    width: 1048px;
    height: 63px;
    background: var(--green);
    display: flex;
    align-items: center;
    justify-content: center;
    gap: 20px;
    padding-top: 6px;
  }
  .person-name {
    font-family: "Urbanist", "Century Gothic", sans-serif;
    font-weight: 700;
    font-size: 48px;
    letter-spacing: 0.3px;
  }
  .dash { font-size: 30px; }
  .person-role { font-size: 32px; }
  .contact-panel {
    position: absolute;
    left: 0;
    top: 378px;
    width: 1048px;
    height: 223px;
    background: var(--ink);
    color: var(--paper);
  }
  .contact-line {
    position: absolute;
    display: flex;
    align-items: center;
    font-size: 29px;
    white-space: nowrap;
  }
  .contact-line svg { fill: var(--paper); flex: none; }
  .contact-phone { left: 420px; top: 40px; gap: 24px; }
  .contact-email { left: 377px; top: 98px; gap: 16px; }
  .contact-web { left: 386px; top: 148px; gap: 18px; }
</style>
</head>
<body>
  <main class="card">
    <div class="brand">
      <span class="brand-square"></span>
      <span class="brand-name">Verum Lawns and Grounds</span>
    </div>

    <div class="name-band">
      <span class="person-name">Dace Marlowby</span>
      <span class="dash">-</span>
      <span class="person-role">Managing Director</span>
    </div>

    <section class="contact-panel">
      <div class="contact-line contact-phone">
        <svg width="22" height="38" viewBox="0 0 22 38" aria-hidden="true">
          <rect x="14" y="0" width="3" height="6"/>
          <rect x="1" y="5" width="20" height="33" rx="3"/>
          <rect x="4" y="9" width="14" height="9" fill="#000"/>
          <g fill="#000">
            <rect x="4" y="21" width="3" height="3"/><rect x="9.5" y="21" width="3" height="3"/><rect x="15" y="21" width="3" height="3"/>
            <rect x="4" y="26" width="3" height="3"/><rect x="9.5" y="26" width="3" height="3"/><rect x="15" y="26" width="3" height="3"/>
            <rect x="4" y="31" width="3" height="3"/><rect x="9.5" y="31" width="3" height="3"/><rect x="15" y="31" width="3" height="3"/>
          </g>
        </svg>
        <span>0413 286 451</span>
      </div>
      <div class="contact-line contact-email">
        <svg width="38" height="24" viewBox="0 0 38 24" aria-hidden="true">
          <rect x="0" y="0" width="38" height="24"/>
          <polyline points="1,1 19,14 37,1" fill="none" stroke="#000" stroke-width="2"/>
          <polyline points="1,23 14,10" fill="none" stroke="#000" stroke-width="1.5"/>
          <polyline points="37,23 24,10" fill="none" stroke="#000" stroke-width="1.5"/>
        </svg>
        <span>dace@vrum.com.au</span>
      </div>
      <div class="contact-line contact-web">
        <svg width="36" height="36" viewBox="0 0 36 36" aria-hidden="true">
          <circle cx="18" cy="18" r="17"/>
          <circle cx="18" cy="18" r="14" fill="#000"/>
          <path d="M9 9 q6 -3 9 2 q-2 4 -6 4 q-1 4 2 7 q-1 5 -3 6 q-4 -3 -5 -9 q0 -6 3 -10z"/>
          <path d="M21 7 q6 1 9 7 q-3 1 -5 -1 q-3 1 -3 5 q5 1 6 5 q-2 5 -6 6 q1 -5 -3 -7 q-2 -4 0 -8 q-2 -3 2 -7z"/>
        </svg>
        <span>www.vrum.com.au</span>
      </div>
    </section>
  </main>
</body>
</html>
```